Black Friday Sale Social Media Graphics

Focusing on Black Friday Graphics for each of the pics attached.  So need the product pics turned into  social media graphics (square size). For the color scheme of the graphics, they should all be complementary to the product colors.
You can add any of the stock photography attached but none are required. I mainly need BOLD text that says:
Black Friday Sale
Up to $15 Off
If you wanted to add smaller text, these headlines can work:
1.	Burn Belly Fat Fast!
2.	Double Your Weight Loss With Our Supplements!
3.	Lose Weight Naturally: Ditch the Prescription Pills & Needles!
4.	Tired of Stubborn Belly Fat? Discover What Works!
5.	Melt Away Belly Fat Faster with Our Supplements!
6.	Struggling to Lose Weight? Discover the Ultimate Solution!
7.	Ready to Burn Fat Faster?

Target Market(s)
women trying to lose weight
Industry/Entity Type
health and wellness
Requirements
Must have
- the product pics attached

Nice to have
- Bold text that says: Black Friday Sale

```html
<!DOCTYPE html>
<html lang="en">
<head>
<meta charset="utf-8">
<title>Black Friday Sale – Social Graphic</title>
<link rel="stylesheet" href="https://fonts.googleapis.com/css2?family=Bebas+Neue&family=Raleway:wght@600&display=swap">
<style>
  :root {
    --plum: #620052;
    --plum-light: #7c0a70;
    --plum-badge: #6d0b5d;
    --pink: #f5b8d8;
    --white: #ffffff;
    --ink: #111111;
    --shelf: #5c5c5c;
  }
  * { margin: 0; padding: 0; box-sizing: border-box; }
  html, body { width: 1200px; height: 1184px; overflow: hidden; background: var(--plum); }
  .sale-graphic {
    position: relative;
    width: 1200px;
    height: 1184px;
    overflow: hidden;
    background: var(--plum);
    font-family: "Bebas Neue", "Oswald", sans-serif;
  }
  .backdrop { position: absolute; inset: 0; }
  .discount-badge {
    position: absolute;
    left: 68px; top: 127px;
    width: 420px; height: 420px;
  }
  .discount-badge .badge-text {
    position: absolute; inset: 0;
    display: flex; flex-direction: column; align-items: center; justify-content: center;
    color: var(--pink);
    line-height: 0.82;
    padding-top: 6px;
  }
  .badge-percent { font-size: 214px; letter-spacing: -2px; }
  .badge-label { font-size: 78px; letter-spacing: -1px; margin-top: 14px; }
  .headline-black,
  .headline-sale {
    position: absolute;
    color: var(--white);
    line-height: 1;
    font-weight: 400;
    text-shadow: 4px 3px 0 #1a0016;
  }
  .headline-black { right: 18px; top: 36px; font-size: 296px; letter-spacing: -4px; }
  .headline-sale { right: 18px; top: 446px; font-size: 300px; letter-spacing: -4px; }
  .friday-band {
    position: absolute;
    left: 596px; top: 282px;
    width: 588px; height: 200px;
    background: var(--pink);
    transform: rotate(-3deg);
    display: flex; align-items: center; justify-content: center;
  }
  .friday-band span {
    color: var(--plum-badge);
    font-size: 238px;
    letter-spacing: -3px;
    line-height: 1;
    padding-top: 22px;
  }
  .tagline {
    position: absolute;
    left: 667px; top: 704px;
    width: 508px; height: 59px;
    background: var(--white);
    display: flex; align-items: center; justify-content: center;
    font-family: "Raleway", "Montserrat", sans-serif;
    font-weight: 600;
    font-size: 43px;
    color: var(--ink);
    letter-spacing: -1px;
    white-space: nowrap;
  }
  .product-shelf {
    position: absolute;
    left: 1009px; top: 1132px;
    width: 191px; height: 52px;
    background: var(--shelf);
  }
  .product-lineup {
    position: absolute;
    left: 662px; top: 880px;
    width: 528px; height: 294px;
    border-radius: 26px 26px 14px 14px;
    background: linear-gradient(100deg, #e9e6ea 0%, #ffffff 30%, #f4f2f4 60%, #ffffff 80%, #ebe7ec 100%);
    box-shadow: 0 4px 14px rgba(0,0,0,0.25);
  }
</style>
</head>
<body>
<main class="sale-graphic">
  <svg class="backdrop" width="1200" height="1184" viewBox="0 0 1200 1184">
    <defs>
      <radialGradient id="badge-glow" cx="278" cy="337" r="330" gradientUnits="userSpaceOnUse">
        <stop offset="0" stop-color="#a4478f" stop-opacity="0.8"/>
        <stop offset="0.7" stop-color="#7c1a6c" stop-opacity="0.4"/>
        <stop offset="1" stop-color="#620052" stop-opacity="0"/>
      </radialGradient>
      <linearGradient id="curl-shade" x1="560" y1="600" x2="430" y2="1000" gradientUnits="userSpaceOnUse">
        <stop offset="0" stop-color="#ffffff"/>
        <stop offset="0.4" stop-color="#d2d2d2"/>
        <stop offset="1" stop-color="#8e8e8e"/>
      </linearGradient>
      <linearGradient id="photo-tone" x1="0" y1="700" x2="700" y2="1184" gradientUnits="userSpaceOnUse">
        <stop offset="0" stop-color="#7c0a70"/>
        <stop offset="0.5" stop-color="#8a3d4a"/>
        <stop offset="1" stop-color="#7c0a70"/>
      </linearGradient>
      <filter id="fold-shadow" x="-10%" y="-10%" width="120%" height="130%">
        <feDropShadow dx="0" dy="6" stdDeviation="8" flood-color="#000" flood-opacity="0.35"/>
      </filter>
    </defs>
    <rect width="1200" height="1184" fill="var(--plum)"/>
    <rect role="img" aria-label="Photo of a slim woman's midriff in white sportswear, hands on hips"
          x="0" y="590" width="800" height="594" fill="url(#photo-tone)"/>
    <path class="page-curl" d="M150 690 C 290 860 470 1030 774 1184 L 800 1184 C 680 1010 600 830 560 597 Z"
          fill="url(#curl-shade)"/>
    <path class="top-sheet" filter="url(#fold-shadow)"
          d="M0 0 H1200 V1184 H800 C 680 1010 600 830 560 597 C 500 680 380 705 267 704 C 160 700 70 660 0 611 Z"
          fill="var(--plum)"/>
    <circle cx="278" cy="337" r="330" fill="url(#badge-glow)"/>
  </svg>

  <div class="discount-badge">
    <svg width="420" height="420" viewBox="0 0 420 420" aria-hidden="true">
      <circle cx="210" cy="210" r="196" fill="none" stroke="var(--white)" stroke-width="18"
              stroke-linecap="round" stroke-dasharray="0 25.6"/>
      <circle cx="210" cy="210" r="192" fill="var(--white)"/>
      <circle cx="210" cy="210" r="184" fill="var(--plum-badge)"/>
    </svg>
    <div class="badge-text">
      <span class="badge-percent">50%</span>
      <span class="badge-label">Discount</span>
    </div>
  </div>

  <h1 class="headline-black">BLACK</h1>
  <div class="friday-band"><span>FRIDAY</span></div>
  <div class="headline-sale">SALE</div>
  <p class="tagline">BURN BELLY FAT FAST!</p>

  <div class="product-shelf"></div>
  <div class="product-lineup" role="img" aria-label="Product photo: row of four white supplement bottles with colored labels"></div>
</main>
</body>
</html>
```